"Wild for Discovery" Summer Camp flyer for preschool

I need a flyer for our preschool's summer camp. Our summer theme is WILD for DISCOVERY. the theme MUST be displayed. We would like a mad scientist with crazy hair look with test tubes and goggles PROMINENTLY DISPLAYED on the flyer. this is for a preschool so we don't want the scientist to look scary. Our logo needs to be included on the flyer. The age range for the school is 6weeks to 6 years (you can add "6 weeks to 6 years" somewhere small on the flyer). Please add "Camp starts June 5th" and Sign up for 1 camp or all!". The weekly themes for the camp are ...
Journey into Outer Space
Rock Out in Geology
Weather
Water Extravagnaza
Biology
Physics - Force & Motion
Light
Sensational Sounds
Budding Builders
Krazy Kitchen Chemistry
Electromagnetism
It's Hip to Be Healthy
we don't want these on the flyer but maybe you can use them for image inspiration.
Attached is our logo and some verbiage that can be used.

moms and dads of preschool age kids

Preschool

• our logo, title of the camp, dates, a Mad Scientist with crazy hair, test tube, and goggles. attached is image of scientist. i will purchase this once art is approved.
• it would be nice to have the weekly themes on the flyer

```html
<!DOCTYPE html>
<html lang="en">
<head>
<meta charset="utf-8">
<title>Wild for Discovery – Summer Camp Flyer</title>
<link rel="stylesheet" href="https://fonts.googleapis.com/css2?family=Walter+Turncoat&family=Ubuntu:wght@300;400&family=Source+Sans+3:wght@600;700&display=swap">
<style>
  :root {
    --page-bg: #e4e4e4;
    --paper-light: #fbfbfb;
    --paper-shade: #e9e9e9;
    --ink: #111111;
    --ink-soft: #2a2a2a;
    --band: #000000;
    --band-text: #ffffff;
    --frame: #3a3a3a;
    --cell-top: #f6f6f6;
    --cell-bottom: #e3e3e3;
    --cell-edge: #b9b9b9;
    --photo-light: #d8d3d0;
    --photo-dark: #8a7f7a;
    --glass-light: #cfc8c4;
    --glass-dark: #8d7f79;
  }
  * { margin: 0; padding: 0; box-sizing: border-box; }
  html, body { width: 1200px; height: 1200px; overflow: hidden; }
  body { background: var(--page-bg); position: relative; }

  .flyer {
    position: absolute;
    left: 174px; top: 0;
    width: 858px; height: 1210px;
    transform: scale(0.9917);
    transform-origin: top left;
    background: radial-gradient(ellipse at 50% 45%, var(--paper-light) 0%, var(--paper-shade) 100%);
    box-shadow: 0 6px 18px rgba(0,0,0,0.18);
  }

  .title-band {
    position: absolute; left: 33px; top: 47px;
    width: 477px; height: 83px;
    background: var(--band);
    color: var(--band-text);
    font-family: "Walter Turncoat", cursive;
    font-size: 40px; letter-spacing: 1px;
    display: flex; align-items: center; justify-content: center;
    white-space: nowrap;
  }

  .age-range {
    position: absolute; left: 41px; top: 150px; width: 452px;
    font-family: "Ubuntu", sans-serif; font-weight: 300;
    font-size: 29px; line-height: 38px; letter-spacing: 2px;
    color: var(--ink-soft);
    text-align: justify; text-align-last: left;
  }

  .camp-dates {
    position: absolute; left: 66px; top: 243px;
    font-family: "Walter Turncoat", cursive;
    font-size: 27px; letter-spacing: 1px; color: var(--ink-soft);
  }

  .scientist-photo {
    position: absolute; left: 508px; top: 43px;
    width: 312px; height: 312px; border-radius: 50%;
    border: 5px solid var(--ink);
    background: radial-gradient(circle at 50% 40%, var(--photo-light) 0%, var(--photo-dark) 100%);
  }

  .themes-band {
    position: absolute; left: 46px; top: 302px;
    width: 475px; height: 56px;
    background: var(--band); color: var(--band-text);
    font-family: "Source Sans 3", sans-serif; font-weight: 600;
    font-size: 26px;
    display: flex; align-items: center; justify-content: center;
  }

  .schedule {
    position: absolute; left: 39px; top: 377px;
    width: 764px; height: 665px;
    border: 2px solid var(--frame); border-radius: 14px;
    padding: 21px 19px 0 19px;
  }
  .schedule-row {
    display: grid; grid-template-columns: 282px 427px; column-gap: 14px;
    height: 43px; margin-bottom: 9.6px;
  }
  .schedule-cell {
    background: linear-gradient(var(--cell-top), var(--cell-bottom));
    border-bottom: 2px solid var(--cell-edge);
    border-right: 2px solid var(--cell-edge);
    font-family: "Source Sans 3", sans-serif; font-weight: 700;
    font-size: 24px; color: var(--ink);
    display: flex; align-items: center;
  }
  .schedule-cell.week { padding-left: 40px; }
  .schedule-cell.theme { padding-left: 19px; }

  .contact-box {
    position: absolute; left: 46px; top: 1070px;
    width: 757px; height: 115px;
    border: 2px solid var(--frame); border-radius: 14px;
  }
  .glassware-art {
    position: absolute; left: 6px; top: 9px;
    width: 225px; height: 93px;
    background: linear-gradient(to top, var(--glass-dark) 0%, var(--glass-light) 100%);
    border-radius: 6px;
  }
  .call-us {
    position: absolute; left: 245px; top: 16px; width: 480px;
    font-family: "Source Sans 3", sans-serif; font-weight: 700;
    font-size: 43px; line-height: 48px; color: var(--ink);
    text-align: center; white-space: nowrap;
  }
  .website {
    position: absolute; left: 245px; top: 66px; width: 480px;
    font-family: "Ubuntu", sans-serif; font-weight: 400;
    font-size: 26px; letter-spacing: 6px; color: var(--ink-soft);
    text-align: center;
  }
</style>
</head>
<body>
  <main class="flyer">
    <h1 class="title-band">WILD for DISCOVERY</h1>
    <p class="age-range">The age range for the school is 6weeks to 6 years</p>
    <p class="camp-dates">JUNE 5TH - AUGUST 28TH</p>
    <div class="scientist-photo" role="img" aria-label="Photo of a friendly mad scientist with wild hair and goggles looking into a microscope beside test tubes and flasks"></div>

    <h2 class="themes-band">The weekly themes for the camp are</h2>

    <section class="schedule">
      <div class="schedule-row"><div class="schedule-cell week">June 5-June 9</div><div class="schedule-cell theme">Journey into Outer Space</div></div>
      <div class="schedule-row"><div class="schedule-cell week">June 12-June 16</div><div class="schedule-cell theme">Rock Out in Geology</div></div>
      <div class="schedule-row"><div class="schedule-cell week">June 19-June 23</div><div class="schedule-cell theme">Weather</div></div>
      <div class="schedule-row"><div class="schedule-cell week">June 24-June 30</div><div class="schedule-cell theme">Water Extravagnaza</div></div>
      <div class="schedule-row"><div class="schedule-cell week">July 3-June 7</div><div class="schedule-cell theme">Biology</div></div>
      <div class="schedule-row"><div class="schedule-cell week">July 10-July 14</div><div class="schedule-cell theme">Physics - Force &amp; Motion</div></div>
      <div class="schedule-row"><div class="schedule-cell week">July 17-July 21</div><div class="schedule-cell theme">Light</div></div>
      <div class="schedule-row"><div class="schedule-cell week">July 24-July 28</div><div class="schedule-cell theme">Sensational Sounds</div></div>
      <div class="schedule-row"><div class="schedule-cell week">July 31-Aug 4</div><div class="schedule-cell theme">Budding Builders</div></div>
      <div class="schedule-row"><div class="schedule-cell week">Aug 7-Aug 11</div><div class="schedule-cell theme">Krazy Kitchen Chemistry</div></div>
      <div class="schedule-row"><div class="schedule-cell week">Aug 14-Aug 28</div><div class="schedule-cell theme">Electromagnetism</div></div>
      <div class="schedule-row"><div class="schedule-cell week">Aug 21-Aug 25</div><div class="schedule-cell theme">It's Hip to Be Healthy</div></div>
    </section>

    <footer class="contact-box">
      <div class="glassware-art" role="img" aria-label="Illustration of laboratory glassware: flasks, beakers and test tubes"></div>
      <p class="call-us">CALL US: 000-000-0000</p>
      <p class="website">www.yourdomain.com</p>
    </footer>
  </main>
</body>
</html>
```